Web Design Project

I need designs (PSD only - no programming) for several pages of a new website helping train operators to manage key information about their traindrivers.
The main feature of this website is the management of personnel records (create, edit, search, delete). Another key aspect is the management of user privileges. Since this is a new website we also need a user friendly frontpage, pricing information and how it works sections.
This can be broken down into 9 pages for which we need designs (PSDs).
1. Home
2. Driver record
3. How it works
4. Pricing
5. User administration
6. Help
7. Record list view
8. Login
9. Registration
Navigation (not logged in) are: Home | How it works | Pricing | Customers | About us | Contact
Navigation (logged in) are: Overview | Administration | Manage records | Billing | Help | Contact
Footer: Customer logos | Awards | Terms & Conditions | Privacy
To provide the best support for you to come up with a strong design proposal I will provide DAILY feedback to all participants. We have also created concept mockups (attached) and example pages (below) for each section to give you a clear sense of what we look for.
The core concepts for a successful bid are that the website is EASY to understand, INTUITIVE to navigate, and SIMPLE to use. Most of our users lack technical background and are looking for tool to simplify their work.
The strongest participants (winner and close contenders) will have the opportunity to additional commissioned work on additional sections not included in this brief.
Example Pages (by section)
1. http://www.quorvane.example/site-keepers/
1. http://www.vrm.example/
1. http://www.tovasko.example/
1. http://www.glimmerhootz.example/
2. http://www.pendlo.example/profile_edit.gne
3. https://www.drav.example/how-it-works/
3. http://www.wexalot.example/learn
4. http://www.brindlequay.example/crm/editions-pricing.jsp
4. http://www.quorvane.example/site-keepers/rates
6. https://support.zoltu.example/en-gb/
6. http://help.harbenquill.example/contact_us
8. https://www.morvelnet.example/uas/login
8. https://www.harbenquill.example/login
8. http://www.ublix.example/login/index
For form designs we like Ferrowen, Okvo, Pendlo, Morvelnet, Trellimap and the concepts presented by Dario Fenstermack in his classic Panel Craft Beyond the Checkboxes.
For additional guidance see mockups attached!
Target Market(s)
Security, human resources and admin support employees for train operators.
Industry/Entity Type
Learn
Requirements
Should not have
- Home page should not have
Social media icons (trellimap, pellomb, Morvelnet, RSS feed)
Contact forms
Read more links
Old trains

```html
<!DOCTYPE html>
<html lang="en">
<head>
<meta charset="utf-8">
<title>How it Works – RailRoster</title>
<link href="https://fonts.googleapis.com/css2?family=Arimo:wght@400;700&family=Sorts+Mill+Goudy&family=Libre+Baskerville:wght@400;700&family=Crimson+Text:wght@700&display=swap" rel="stylesheet">
<style>
:root{
  --brand:#2a5d95;
  --link:#1f6fa8;
  --ink:#333;
  --band-a:#2a5f98;
  --band-b:#2384c9;
  --slate:#8e8e8e;
  --accent:#c96b56;
  --rule:#e2e2e2;
  --tile:#cdc9b8;
  --footer:#353535;
  --footer-top:#4a4a4a;
  --footer-text:#b5b5b5;
  --btn-blue:#2f6aa6;
  --social:#6a6a6a;
}
*{box-sizing:border-box;margin:0;padding:0}
html,body{width:1200px;height:1200px;overflow:hidden;background:#fff;font-family:"Arimo",Arial,sans-serif;color:var(--ink)}
.page{position:relative;width:1200px;height:1200px}
.abs{position:absolute}

/* header */
.brand-mark{left:28px;top:22px;width:22px;height:22px;background:var(--brand)}
.brand-name{left:58px;top:18px;font:700 30px/1 "Arimo",Arial,sans-serif;color:var(--brand)}
.brand-tag{left:33px;top:77px;font:400 16px/1 "Arimo",Arial,sans-serif;color:#8a8a8a}
.nav{top:42px;font:700 11px/1 "Libre Baskerville",Georgia,serif;color:#4a4a4a}
.nav.current{color:var(--link);border-bottom:2px solid #3a9ad9;padding-bottom:4px}
.account-tab{left:1018px;top:4px;width:190px;height:24px;border-radius:5px 0 0 5px;background:linear-gradient(#2e6ba6,#1f558c);color:#fff;font:700 11px/24px "Crimson Text",Georgia,serif;padding-left:6px;white-space:nowrap}
.field{border:1px solid #dcdcdc;border-radius:3px;background:#fff;font:400 8px/1 "Arimo",Arial,sans-serif;color:#aaa;letter-spacing:.6px;padding:9px 10px}
.top-field{left:1018px;width:190px;height:25px}

/* hero */
.band{left:0;top:104px;width:1200px;height:251px;background:linear-gradient(90deg,var(--band-a),var(--band-b) 50%,var(--band-a))}
.band::before{content:"";position:absolute;left:0;right:0;top:0;height:3px;background:linear-gradient(90deg,transparent,#55c0ef,transparent)}
.slider{left:248px;top:120px;width:704px;height:255px;border-radius:4px;overflow:hidden;box-shadow:0 3px 6px rgba(0,0,0,.2)}
.slide-copy{left:0;top:0;width:308px;height:255px;background:var(--slate)}
.slide-copy p{position:absolute;left:35px;top:87px;width:250px;font:400 11px/16px "Arimo",Arial,sans-serif;color:#fff;letter-spacing:.6px}
.slide-copy b{font-weight:700;font-size:12px}
.cta{position:absolute;left:0;top:181px;width:185px;height:35px;background:var(--accent);border-radius:0 4px 4px 0;color:#fff;font:400 14px/35px "Arimo",Arial,sans-serif;padding-left:14px}
.dots{position:absolute;left:14px;top:234px;display:flex;gap:5px}
.dots span{width:11px;height:11px;border-radius:50%;background:#fff;border:3px solid #444}
.dots span.on{border-color:#3a9ad9}
.slide-photo{left:308px;top:0;width:396px;height:255px;background:linear-gradient(#3f6fb4 0%,#4b7fc2 55%,#d9e1ea 70%,#f1f3f5 100%)}

/* how it works */
.h-section{left:250px;top:391px;font:700 18px/1 "Libre Baskerville",Georgia,serif;color:#111}
.rule{height:1px;background:var(--rule);left:250px;width:700px}
.col-title{font:400 17px/1 "Sorts Mill Goudy",Georgia,serif;color:var(--link);top:449px}
.col-sub{font:400 9px/1 "Arimo",Arial,sans-serif;color:#888;top:467px}
.frame{top:490px;width:224px;height:148px;background:#fff;border:1px solid #e4e4e4;box-shadow:0 1px 3px rgba(0,0,0,.1);padding:5px}
.frame div{width:100%;height:100%}
.col-text{top:644px;width:224px;font:400 10px/14px "Arimo",Arial,sans-serif;color:#444;letter-spacing:.5px}
.btn-light{top:727px;width:122px;height:24px;border:1px solid #ddd;border-radius:3px;background:linear-gradient(90deg,#fff,#ececec);font:400 9px/22px "Arimo",Arial,sans-serif;color:var(--link);padding-left:9px}
.arrow{position:absolute;right:9px;top:7px}

/* lower area */
.h-small{font:400 14px/1 "Sorts Mill Goudy",Georgia,serif;color:#333}
.dotted{height:0;border-top:1px dashed #cfcfcf;width:222px}
.tile{top:863px;width:38px;height:38px;border-radius:5px;background:var(--tile)}
.newsletter-h{left:251px;top:931px;font:700 12px/1 "Libre Baskerville",Georgia,serif;color:#222}
.small-text{font:400 9px/11px "Arimo",Arial,sans-serif;color:#444}
.btn-blue{top:1021px;width:122px;height:25px;border-radius:3px;background:linear-gradient(90deg,var(--btn-blue),#6d9cc9);color:#fff;font:400 11px/25px "Sorts Mill Goudy",Georgia,serif;padding-left:10px}
.thumb{left:728px;width:44px;height:44px;border:1px solid #ddd;background:#fff;padding:4px}
.thumb div{width:100%;height:100%}

/* footer */
.footer{left:0;top:1062px;width:1200px;height:138px;background:var(--footer);border-top:7px solid var(--footer-top)}
.foot-text{font:400 10px/1 "Arimo",Arial,sans-serif;color:var(--footer-text)}
.social{right:12px;top:1153px;display:flex;gap:8px}
.social span{display:block;width:28px;height:28px;border-radius:5px;background:var(--social)}
</style>
</head>
<body>
<div class="page">

  <header>
    <div class="abs brand-mark"></div>
    <div class="abs brand-name">RailRoster</div>
    <div class="abs brand-tag">tageline place here</div>

    <nav>
      <span class="abs nav" style="left:490px">Home</span>
      <span class="abs nav current" style="left:539px">How it Works</span>
      <span class="abs nav" style="left:631px">Prices</span>
      <span class="abs nav" style="left:685px">Our Customers</span>
      <span class="abs nav" style="left:794px">About Us</span>
      <span class="abs nav" style="left:866px">Contact</span>
    </nav>

    <div class="abs account-tab">Signup | Login | Language (English)</div>
    <div class="abs field top-field" style="top:36px">your name</div>
    <div class="abs field top-field" style="top:73px">your email address</div>
  </header>

  <section class="hero">
    <div class="abs band"></div>
    <div class="abs slider">
      <div class="abs slide-copy">
        <p>Security, <b>human resources</b> and admin support employees for train operators</p>
        <div class="cta">Signup or request a Call</div>
        <div class="dots"><span></span><span class="on"></span><span></span></div>
      </div>
      <div class="abs slide-photo" role="img" aria-label="Photo of a businessman in a blue shirt holding a chain of paper cut-out figures"></div>
    </div>
  </section>

  <section class="how">
    <h1 class="abs h-section">How it Works</h1>
    <div class="abs rule" style="top:422px"></div>

    <h2 class="abs col-title" style="left:250px">Our Work</h2>
    <div class="abs col-sub" style="left:250px">All you want your website to do.</div>
    <div class="abs frame" style="left:248px"><div role="img" aria-label="Close-up photo of a login screen with user name field" style="background:linear-gradient(135deg,#f3f6f2,#c9d8cf 60%,#e9efe9)"></div></div>
    <p class="abs col-text" style="left:251px">Sed ut perspiciatis unde omnis iste natus error sit voluptatem accusantium doloremque laudantium, totam rem aperiam, eaque ipsa quae ab illo inventore veritatis et quasi architecto beatae vitae dicta sunt</p>
    <div class="abs btn-light" style="left:251px">Learn More<svg class="arrow" width="14" height="8" viewBox="0 0 14 8"><path d="M0 4h13M9 1l3 3-3 3" stroke="#6a8db3" fill="none"/></svg></div>

    <h2 class="abs col-title" style="left:490px">Our Packages</h2>
    <div class="abs col-sub" style="left:490px">A tool anything and everything you can think</div>
    <div class="abs frame" style="left:488px"><div role="img" aria-label="Photo of colleagues meeting around a laptop on a coffee table" style="background:linear-gradient(160deg,#b7b1a6,#6e6156 55%,#a59e92)"></div></div>
    <p class="abs col-text" style="left:492px">Nemo enim ipsam voluptatem quia voluptas sit aspernatur aut odit aut fugit, sed quia consequuntur magni dolores eos qui ratione voluptatem sequi nesciun tdolore magnam aliquam quaerat voluptatem.</p>
    <div class="abs btn-light" style="left:491px">Learn More<svg class="arrow" width="14" height="8" viewBox="0 0 14 8"><path d="M0 4h13M9 1l3 3-3 3" stroke="#6a8db3" fill="none"/></svg></div>

    <h2 class="abs col-title" style="left:731px">Train Operators</h2>
    <div class="abs col-sub" style="left:731px">Fresh. Modern and ready for future</div>
    <div class="abs frame" style="left:729px"><div role="img" aria-label="Photo of a support operator wearing a headset" style="background:linear-gradient(120deg,#8a96a3,#cdbfae 45%,#3a4c5e)"></div></div>
    <p class="abs col-text" style="left:733px">Neque porro quisquam est, qui dolorem ipsum quia dolor sit amet, consectetur, adipisci velit, sed quia non numquam eius modi tempora incidunt ut labore et dolore magnam aliquam quaerat voluptatem.</p>
    <div class="abs btn-light" style="left:732px">Learn More<svg class="arrow" width="14" height="8" viewBox="0 0 14 8"><path d="M0 4h13M9 1l3 3-3 3" stroke="#6a8db3" fill="none"/></svg></div>

    <div class="abs rule" style="top:777px"></div>
  </section>

  <section class="lower">
    <div class="abs dotted" style="left:251px;top:827px"></div>
    <h3 class="abs h-small" style="left:251px;top:839px">Partner Logos</h3>
    <div class="abs tile" style="left:252px"></div>
    <div class="abs tile" style="left:298px"></div>
    <div class="abs tile" style="left:344px"></div>
    <div class="abs tile" style="left:390px"></div>
    <div class="abs tile" style="left:436px"></div>

    <h3 class="abs newsletter-h">Newsletter</h3>
    <div class="abs dotted" style="left:251px;top:949px"></div>
    <p class="abs small-text" style="left:252px;top:959px;width:222px">At vero eos et accusamus et iusto odio dignissimos ducimus qui blanditiis praesentium</p>
    <div class="abs field" style="left:252px;top:988px;width:222px;height:25px">your email address</div>
    <div class="abs btn-blue" style="left:252px">Subscribe<svg class="arrow" width="14" height="8" viewBox="0 0 14 8" style="top:9px"><path d="M0 4h13M9 1l3 3-3 3" stroke="#fff" fill="none"/></svg></div>

    <h3 class="abs h-small" style="left:488px;top:808px">Contact</h3>
    <div class="abs dotted" style="left:488px;top:827px"></div>
    <div class="abs field" style="left:488px;top:839px;width:222px;height:24px">your name</div>
    <div class="abs field" style="left:488px;top:876px;width:222px;height:24px">your email address</div>
    <div class="abs field" style="left:488px;top:913px;width:222px;height:100px">message</div>
    <div class="abs btn-blue" style="left:490px">Send it<svg class="arrow" width="14" height="8" viewBox="0 0 14 8" style="top:9px"><path d="M0 4h13M9 1l3 3-3 3" stroke="#fff" fill="none"/></svg></div>

    <h3 class="abs h-small" style="left:728px;top:808px">News Updates</h3>
    <div class="abs dotted" style="left:728px;top:827px"></div>
    <div class="abs thumb" style="top:838px"><div style="background:#03a6e6"></div></div>
    <p class="abs small-text" style="left:777px;top:838px;width:175px">Lorem ipsum dolor sit amet, consectetur adipisicing elit, sed do eiusmod tempor incididunt ut labore et dolore magna aliqua.</p>
    <div class="abs dotted" style="left:728px;top:888px"></div>
    <div class="abs thumb" style="top:900px"><div style="background:#2c5e91"></div></div>
    <p class="abs small-text" style="left:777px;top:900px;width:170px">Sed ut perspiciatis unde omnis iste natus error sit voluptatem accusantium doloremque laudantium, totam rem aperiam.</p>
    <div class="abs dotted" style="left:728px;top:950px"></div>
    <div class="abs thumb" style="top:962px"><div style="background:#2c5e91"></div></div>
    <p class="abs small-text" style="left:777px;top:962px;width:165px">At vero eos et accusamus et iusto odio dignissimos ducimus qui blanditiis praesentium.</p>
    <div class="abs dotted" style="left:728px;top:1012px"></div>
    <div class="abs btn-blue" style="left:728px">Visit our Blog<svg class="arrow" width="14" height="8" viewBox="0 0 14 8" style="top:9px"><path d="M0 4h13M9 1l3 3-3 3" stroke="#fff" fill="none"/></svg></div>
  </section>

  <footer>
    <div class="abs footer"></div>
    <p class="abs foot-text" style="left:16px;top:1097px">Copywrite © 2012 RailRoster | All rights reserved | T&amp;C</p>
    <p class="abs foot-text" style="right:10px;top:1081px">Home | How it works | Prices Our Customers | About us | Contact</p>
    <div class="abs social" aria-label="Social links">
      <span></span><span></span><span></span><span></span><span></span>
    </div>
  </footer>

</div>
</body>
</html>
```